Motor Mate 4x6 Flyer

Need 4 x 6 Flyer with following language:

Willow Crest Motor Mate
Our Motor Mate Will Come to Your Home
Our Motor Mate will Drive Your Car to Nearest Gas Station
Our Motor Mate will Fill-up Your Car with Gas
Our Motor Mate will Immediately Return Your Car
Your Car Covered with $100k of Commercial Insurance
Member Dunmore Chamber of Commerce / Honest Merchant League
www.willowcrestmotormate.example

Place logos of Vortan, Brenn & Dorvane on Left Side of Flyer starting at top left corner, mid left side, left bottom corner.
Place logos of BoltNest, 12-Forty, Tesmira on opposite side right.....
Place Willow Crest Motor Mate Logo on both sides of very top that says Willow Crest Motor Mate

Target Market(s)

Upscale Home Owners

Font styles to use
Sans Serif

Colors
F0912C
F2A743
F7CA91
FBE8D2
FDF5EE

Requirements
Must have
• Flyer Must be Bright Orange

```html
<!DOCTYPE html>
<html lang="en">
<head>
<meta charset="utf-8">
<title>Willow Crest Motor Mate – 4x6 Flyer</title>
<link href="https://fonts.googleapis.com/css2?family=Montserrat:wght@700;800;900&family=Open+Sans:wght@400;600&family=Quicksand:wght@500;600;700&display=swap" rel="stylesheet">
<style>
  :root{
    --orange:#f0912c;
    --orange-mid:#f2a743;
    --orange-soft:#f7ca91;
    --orange-pale:#fbe8d2;
    --cream:#fdf5ee;
    --backdrop:#4b4e53;
    --ink:#111213;
    --slate:#5c5f64;
    --strip-top:#e6e7e9;
    --white:#ffffff;
  }
  *{box-sizing:border-box;margin:0;padding:0}
  html,body{width:1200px;height:1200px;overflow:hidden}
  body{background:var(--backdrop);position:relative;font-family:"Open Sans",sans-serif}

  .flyer{position:absolute;left:240px;width:720px;height:480px;overflow:hidden}
  .flyer--front{top:103px}
  .flyer--back{top:617px;background:linear-gradient(180deg,var(--strip-top) 0%,var(--strip-top) 8%,var(--orange-pale) 30%,var(--orange-soft) 55%,var(--orange-mid) 80%,var(--orange) 100%)}

  /* front */
  .hero-photo{position:absolute;inset:0;background:
      radial-gradient(ellipse 40% 55% at 82% 50%,#b7825f 0%,rgba(120,90,75,.6) 40%,rgba(40,45,52,0) 75%),
      linear-gradient(90deg,#0e1418 0%,#1c252c 35%,#3b444b 60%,#6e737a 100%)}
  .front-brand{position:absolute;left:60px;top:150px;font-family:"Quicksand",sans-serif;font-weight:600;font-size:37px;letter-spacing:.5px;color:var(--orange)}
  .front-brand .mark{display:inline-block;width:14px;height:14px;background:var(--orange);margin-right:10px;vertical-align:middle}
  .front-title{position:absolute;left:43px;top:300px;font-family:"Montserrat",sans-serif;font-weight:900;font-size:44px;line-height:46px;text-transform:uppercase}
  .front-title .line-1{color:var(--orange)}
  .front-title .line-2{color:var(--white)}
  .front-title .accent{color:var(--orange)}
  .front-url{position:absolute;left:44px;top:414px;font-family:"Quicksand",sans-serif;font-weight:700;font-size:14.5px;color:var(--white)}

  /* back: partner strip */
  .partner-strip{position:absolute;left:0;top:0;width:150px;height:480px}
  .partner{position:absolute;left:0;width:150px;text-align:center;font-family:"Montserrat",sans-serif;font-weight:800;font-size:13px;color:#2f3033;letter-spacing:.5px}
  .partner::before{content:"";display:inline-block;width:9px;height:9px;background:#2f3033;margin-right:6px;vertical-align:1px}

  /* back: white panel */
  .panel{position:absolute;left:150px;top:15px;width:570px;height:449px;background:var(--white);border-radius:18px 0 0 18px}
  .panel-brand{position:absolute;left:32px;top:98px;font-family:"Quicksand",sans-serif;font-weight:700;font-size:24px;color:var(--orange)}
  .panel-brand .dark{color:var(--orange)}
  .panel-divider{position:absolute;left:207px;top:32px;width:1px;height:95px;background:#cfd1d4}
  .panel-title{position:absolute;left:236px;top:38px;font-family:"Montserrat",sans-serif;font-weight:900;font-size:34px;line-height:39px;color:var(--ink);text-transform:uppercase}
  .panel-title .accent{color:var(--orange)}

  .steps{position:absolute;left:15px;top:160px;width:540px;height:146px}
  .step{position:absolute;top:0;width:124px;height:146px;border:1.5px solid var(--orange-mid);border-radius:8px}
  .step:nth-child(1){left:0}.step:nth-child(2){left:138px}.step:nth-child(3){left:277px}.step:nth-child(4){left:414px}
  .step-icon{position:absolute;left:38px;top:16px;width:48px;height:48px}
  .step-label{position:absolute;left:7px;right:7px;top:80px;height:59px;background:var(--orange);border-radius:2px;display:flex;align-items:center;justify-content:center;text-align:center;color:var(--white);font-size:10px;line-height:12px}
  .step-dot{position:absolute;width:4px;height:4px;border-radius:50%;background:var(--orange-mid)}

  .trust{position:absolute;left:15px;top:322px;width:540px;height:64px}
  .insurance{position:absolute;left:0;top:0;width:193px;height:64px;background:var(--slate);border-radius:8px;color:var(--white);font-size:10px;line-height:12px;font-weight:600;text-align:center}
  .insurance svg{position:absolute;left:16px;top:12px}
  .insurance p{position:absolute;left:58px;right:8px;top:14px}
  .membership{position:absolute;left:213px;top:0;width:327px;height:64px;border:1.5px solid #d6d8db;border-radius:8px;overflow:hidden;background:var(--white)}
  .membership-label{position:absolute;left:0;top:0;width:76px;height:100%;background:var(--slate);color:var(--white);font-size:10px;font-weight:600;display:flex;align-items:center;justify-content:center}
  .badge-chamber{position:absolute;left:96px;top:14px;width:104px;height:34px;background:#2a3f8f;border-radius:2px}
  .badge-league{position:absolute;left:220px;top:15px;width:92px;height:34px;background:#1f5a80;border-radius:4px}

  .url-bar{position:absolute;left:15px;top:402px;width:540px;height:32px;background:var(--orange);border-radius:4px;display:flex;align-items:center;justify-content:center;font-family:"Quicksand",sans-serif;font-weight:700;font-size:13.5px;color:var(--white)}
</style>
</head>
<body>

<section class="flyer flyer--front">
  <div class="hero-photo" role="img" aria-label="Photo: smiling driver giving a thumbs up from the seat of her car"></div>
  <div class="front-brand"><span class="mark"></span>MOTOR MATE</div>
  <h1 class="front-title">
    <span class="line-1">Willow Crest</span><br>
    <span class="line-2">Motor <span class="accent">Mate</span></span>
  </h1>
  <div class="front-url">www.willowcrestmotormate.example</div>
</section>

<section class="flyer flyer--back">
  <div class="partner-strip">
    <div class="partner" style="top:42px">VORTAN</div>
    <div class="partner" style="top:104px">BRENN</div>
    <div class="partner" style="top:179px">DORVANE</div>
    <div class="partner" style="top:255px">BOLTNEST</div>
    <div class="partner" style="top:336px">12-FORTY</div>
    <div class="partner" style="top:424px">TESMIRA</div>
  </div>

  <div class="panel">
    <div class="panel-brand">MOTOR MATE</div>
    <div class="panel-divider"></div>
    <h2 class="panel-title">Willow Crest<br><span class="accent">Motor</span> Mate</h2>

    <div class="steps">
      <div class="step">
        <svg class="step-icon" viewBox="0 0 48 48" fill="none" stroke="#f0912c" stroke-width="2">
          <circle cx="24" cy="24" r="23" stroke="#5c5f64" stroke-width="1.5"/>
          <path d="M24 36c-6-7-9-11-9-15a9 9 0 0 1 18 0c0 4-3 8-9 15z"/>
          <path d="M20 23v-3l4-3 4 3v3z" fill="#f0912c" stroke="none"/>
        </svg>
        <div class="step-label">Our Motor Mate<br>Will Come<br>to Your Home</div>
        <span class="step-dot" style="right:-3px;top:95px"></span>
      </div>
      <div class="step">
        <svg class="step-icon" viewBox="0 0 48 48" fill="none" stroke="#f0912c" stroke-width="2">
          <circle cx="24" cy="24" r="23" stroke="#5c5f64" stroke-width="1.5"/>
          <path d="M15 33v-7l3-5h12l3 5v7zM15 29h18"/>
          <circle cx="19" cy="30" r="1" fill="#f0912c"/><circle cx="29" cy="30" r="1" fill="#f0912c"/>
          <path d="M19 15h10l-2-2M29 18H19l2 2"/>
        </svg>
        <div class="step-label">Our Motor Mate<br>Will Drive Your<br>Car to Nearest<br>Gas Station</div>
        <span class="step-dot" style="left:-3px;top:58px"></span>
        <span class="step-dot" style="right:-3px;top:95px"></span>
      </div>
      <div class="step">
        <svg class="step-icon" viewBox="0 0 48 48" fill="none" stroke="#f0912c" stroke-width="2">
          <circle cx="24" cy="24" r="23" stroke="#5c5f64" stroke-width="1.5"/>
          <path d="M14 22l8-8 9 9-8 8z" fill="#f0912c"/>
          <path d="M33 27c-2 3-2 5 0 5s2-2 0-5z" fill="#f0912c" stroke="none"/>
        </svg>
        <div class="step-label">Our Motor Mate<br>will Fill-up Your<br>Car with Gas</div>
        <span class="step-dot" style="left:-3px;top:58px"></span>
        <span class="step-dot" style="right:-3px;top:95px"></span>
      </div>
      <div class="step">
        <svg class="step-icon" viewBox="0 0 48 48" fill="none" stroke="#f0912c" stroke-width="2">
          <circle cx="24" cy="24" r="23" stroke="#5c5f64" stroke-width="1.5"/>
          <path d="M15 33v-7l3-5h12l3 5v7zM15 29h18"/>
          <circle cx="19" cy="30" r="1" fill="#f0912c"/><circle cx="29" cy="30" r="1" fill="#f0912c"/>
          <path d="M21 16l2 2 4-4"/>
        </svg>
        <div class="step-label">Our Motor Mate<br>Will Immediately<br>Return Your Car</div>
        <span class="step-dot" style="left:-3px;top:58px"></span>
      </div>
    </div>

    <div class="trust">
      <div class="insurance">
        <svg width="32" height="40" viewBox="0 0 32 40" fill="none" stroke="#f0912c" stroke-width="2.5">
          <path d="M16 2l13 5v11c0 9-6 16-13 20C9 34 3 27 3 18V7z"/>
          <path d="M10 20l5 5 8-9"/>
        </svg>
        <p>Your Car Covered<br>with $100k of<br>Commercial Insurance</p>
      </div>
      <div class="membership">
        <div class="membership-label">Member</div>
        <div class="badge-chamber" role="img" aria-label="Dunmore Chamber of Commerce member badge"></div>
        <div class="badge-league" role="img" aria-label="Honest Merchant League accredited business badge"></div>
      </div>
    </div>

    <div class="url-bar">www.willowcrestmotormate.example</div>
  </div>
</section>

</body>
</html>
```